We are looking to design a black on white bourbon label for a new brand
in att we have added
1. the bottle we need to use (wine bottle in black)
2. some industry examples (Look at horse rider label good example of where we need to go)
3. horses and cowboys illistrations

The brand will be Called MARROWGATE RUN. we want an old school feeling label prohibition style.

What we need on the label is
1. visual = Bucking Horse + rider cowboy + lasso forming a circle
2. Name = Marrowgate Run Bourbon Straight Aged Whiskey
3. Product info = 70 CL 40 ABV
4. Distilled in the Wild Wild West WWW.MARROWGATERUNWHISKEY.EXAMPLE

```html
<!DOCTYPE html>
<html lang="en">
<head>
<meta charset="utf-8">
<title>Marrowgate Run Bourbon Label</title>
<link rel="stylesheet" href="https://fonts.googleapis.com/css2?family=Rye&family=Cormorant+Garamond:wght@400;500&display=swap">
<style>
  :root {
    --paper: #ffffff;
    --label: #000000;
    --ink: #ffffff;
    --rule: #8a8a8a;
    --art-light: #6e6e6e;
    --art-dark: #1a1a1a;
    --shadow: rgba(0, 0, 0, 0.35);
  }
  html, body {
    margin: 0;
    padding: 0;
    overflow: hidden;
  }
  body {
    width: 848px;
    height: 1200px;
    background: var(--paper);
    position: relative;
  }
  .label {
    position: absolute;
    left: 78px;
    top: 54px;
    width: 692px;
    height: 1084px;
    background: var(--label);
    box-shadow: 6px 8px 10px var(--shadow);
    color: var(--ink);
  }
  .brand {
    position: absolute;
    left: 0;
    width: 100%;
    margin: 0;
    text-align: center;
    font-family: "Rye", serif;
    font-weight: 400;
    color: var(--ink);
    line-height: 1;
  }
  .brand--top { top: 60px; font-size: 54px; letter-spacing: 1px; }
  .brand--bottom { top: 612px; font-size: 76px; letter-spacing: 4px; }
  .emblem {
    position: absolute;
    left: 105px;
    top: 150px;
    width: 440px;
    height: 440px;
  }
  .spec {
    position: absolute;
    top: 744px;
    font-family: "Cormorant Garamond", serif;
    font-size: 20px;
    letter-spacing: 1px;
    transform: translateX(-50%);
    white-space: nowrap;
  }
  .spec--volume { left: 190px; }
  .spec--strength { left: 459px; }
  .rule {
    position: absolute;
    height: 1px;
    background: var(--rule);
  }
  .product {
    position: absolute;
    left: 0;
    width: 100%;
    text-align: center;
    font-family: "Cormorant Garamond", serif;
    font-weight: 400;
    font-size: 34px;
    letter-spacing: 4px;
    margin: 0;
    line-height: 1;
  }
  .product--line1 { top: 825px; }
  .product--line2 { top: 885px; }
  .origin {
    position: absolute;
    top: 970px;
    left: 0;
    width: 100%;
    text-align: center;
    font-family: "Cormorant Garamond", serif;
    font-variant: small-caps;
    font-size: 21px;
    letter-spacing: 4px;
    line-height: 1;
  }
  .website {
    position: absolute;
    top: 1003px;
    left: 0;
    width: 100%;
    text-align: center;
    font-family: "Cormorant Garamond", serif;
    font-size: 10px;
    letter-spacing: 2px;
    line-height: 1;
  }
</style>
</head>
<body>
  <section class="label">
    <h1 class="brand brand--top">MARROWGATE</h1>

    <svg class="emblem" viewBox="0 0 440 440" role="img" aria-label="Engraved illustration of a cowboy riding a bucking horse inside a circle of lasso rope">
      <defs>
        <radialGradient id="emblemTone" cx="50%" cy="45%" r="55%">
          <stop offset="0%" stop-color="var(--art-light)"/>
          <stop offset="100%" stop-color="var(--art-dark)"/>
        </radialGradient>
      </defs>
      <circle cx="220" cy="220" r="218" fill="url(#emblemTone)"/>
    </svg>

    <h2 class="brand brand--bottom">RUN</h2>

    <span class="spec spec--volume">70 CL</span>
    <span class="spec spec--strength">40% ABV</span>
    <div class="rule" style="left:75px; top:790px; width:240px;"></div>
    <div class="rule" style="left:346px; top:790px; width:228px;"></div>

    <p class="product product--line1">BOURBON STRAIGHT</p>
    <p class="product product--line2">AGED WHISKEY</p>

    <div class="rule" style="left:82px; top:956px; width:257px;"></div>
    <div class="rule" style="left:353px; top:956px; width:223px;"></div>

    <p class="origin" style="margin:0;">Distilled In The Wild West</p>
    <p class="website" style="margin:0;">WWW.MARROWGATERUNWHISKEY.EXAMPLE</p>

    <div class="rule" style="left:78px; top:1031px; width:237px;"></div>
    <div class="rule" style="left:350px; top:1031px; width:225px;"></div>
  </section>
</body>
</html>
```